Website Design - Financial Services Software

We are looking for website designs for our public website.
Some competitor sites we like are
www.torvani.com.au
www.pluma.com.au
www.quentabridge.com
www.morlupa.com.au

A wireframe example of our site can be found at
http://pr4tqz.bivlowpage.com/

Attached is our logo.

Industry/Entity Type

Financial

```html
<!DOCTYPE html>
<html lang="en">
<head>
<meta charset="utf-8">
<title>Valtoria – Smarter Financial Strategies</title>
<link rel="stylesheet" href="https://fonts.googleapis.com/css2?family=Open+Sans:wght@300;400;600;700&family=Lato:wght@400;700;900&display=swap">
<style>
  :root {
    --gold: #b8862a;
    --gold-light: #e2c25a;
    --gold-dark: #8a5a12;
    --brown: #7b4a10;
    --navy: #1d2a3a;
    --ink: #333333;
    --text: #444444;
    --muted: #5a5a5a;
    --page: #f7f7f7;
    --white: #ffffff;
    --footer: #333333;
    --video-dark: #3e4548;
    --yellow: #f2e06a;
    --blue: #1a9ad6;
  }
  * { box-sizing: border-box; margin: 0; padding: 0; }
  html, body { width: 1200px; height: 1080px; overflow: hidden; }
  body { position: relative; background: var(--white); font-family: "Open Sans", sans-serif; color: var(--ink); }
  .abs { position: absolute; }

  /* Header */
  .site-header { position: absolute; left: 0; top: 0; width: 1200px; height: 79px;
    background: linear-gradient(#ffffff, #ececec); border-bottom: 1px solid #cfcfcf; }
  .brand { position: absolute; left: 141px; top: 14px; display: flex; align-items: center; gap: 10px; }
  .brand-square { width: 44px; height: 44px; background: var(--gold); }
  .brand-name { font-family: "Open Sans", sans-serif; font-weight: 600; font-size: 30px; letter-spacing: 2px; color: var(--gold); line-height: 1; }
  .brand-tag { font-size: 9.5px; letter-spacing: 1px; color: var(--navy); margin-top: 3px; }
  .login { position: absolute; left: 974px; top: 9px; width: 85px; height: 27px; border-radius: 14px;
    background: var(--gold); color: var(--white); font-family: "Lato", sans-serif; font-weight: 700; font-size: 15px;
    text-align: center; line-height: 27px; }
  .main-nav a { position: absolute; top: 49px; font-family: "Lato", sans-serif; font-weight: 700; font-size: 15px;
    color: var(--navy); text-decoration: none; letter-spacing: .3px; }
  .main-nav a.active { color: var(--gold-dark); }

  /* Hero */
  .hero { position: absolute; left: 0; top: 79px; width: 1200px; height: 436px; }
  .hero-photo { position: absolute; inset: 0;
    background: radial-gradient(ellipse at 30% 40%, #e8c9b8 0%, transparent 45%),
                radial-gradient(ellipse at 85% 20%, #4a5560 0%, transparent 30%),
                radial-gradient(ellipse at 60% 80%, #c8d4de 0%, transparent 50%),
                linear-gradient(120deg, #dfe6ec, #c9d3dc 40%, #e9e2dc 70%, #aeb8c2); }
  .intro-panel { position: absolute; left: 141px; top: 73px; width: 466px; height: 323px;
    background: linear-gradient(#ffffff 0%, rgba(255,255,255,.92) 30%, rgba(200,214,226,.85) 100%);
    border: 1px solid rgba(255,255,255,.8); }
  .intro-band { height: 53px; background: linear-gradient(#c9952f, #e7c251 50%, #b98628); }
  .intro-title { position: absolute; left: 88px; top: 11px; font-size: 26px; font-weight: 600; color: #4a3512; }
  .intro-lead { position: absolute; right: 19px; top: 64px; width: 400px; text-align: right; font-size: 21px; line-height: 24px; color: #222; }
  .btn-tour { position: absolute; left: 167px; top: 123px; width: 132px; height: 26px; border-radius: 13px;
    background: linear-gradient(#e5c04e, #b98628); color: var(--white); font-family: "Lato", sans-serif; font-weight: 700;
    font-size: 15px; text-align: center; line-height: 26px; box-shadow: 0 1px 2px rgba(0,0,0,.3); }
  .audience-card { position: absolute; top: 162px; width: 202px; height: 142px;
    background: var(--gold); clip-path: polygon(0 0,100% 0,100% 82%,50% 100%,0 82%); }
  .audience-card .photo { position: absolute; left: 5px; top: 28px; right: 5px; bottom: 5px;
    clip-path: polygon(0 0,100% 0,100% 79%,50% 100%,0 79%);
    background: linear-gradient(135deg, #d9dde2, #8a8f98 50%, #eef0f2); }
  .audience-card .label { position: absolute; left: 5px; right: 5px; top: 0; height: 28px; background: var(--gold-dark);
    color: var(--white); font-family: "Lato", sans-serif; font-weight: 700; font-size: 13.5px; text-align: center; line-height: 28px; }

  .video-panel { position: absolute; left: 647px; top: 72px; width: 412px; height: 324px;
    border: 4px solid #8e9296; background: radial-gradient(circle at 50% 45%, #ffffff, #e6e6e6); }
  .video-thumb { position: absolute; left: 10px; top: 9px; width: 55px; height: 55px; background: var(--video-dark); }
  .video-title { position: absolute; left: 68px; top: 9px; width: 211px; height: 21px; background: var(--video-dark);
    color: var(--yellow); font-weight: 700; font-size: 13px; line-height: 21px; padding-left: 4px; }
  .video-from { position: absolute; left: 68px; top: 32px; height: 16px; background: var(--video-dark); color: var(--white);
    font-size: 11px; line-height: 16px; padding: 0 4px; }
  .video-from span { color: var(--yellow); }
  .video-action { position: absolute; left: 353px; width: 40px; height: 32px; border-radius: 4px; background: var(--video-dark);
    color: var(--white); font-size: 7px; font-weight: 700; text-align: center; }
  .video-action svg { display: block; margin: 4px auto 1px; }
  .video-brand { position: absolute; left: 0; right: 0; top: 196px; text-align: center; }
  .video-brand .name { font-size: 40px; font-weight: 600; letter-spacing: 3px; color: var(--gold); line-height: 1; }
  .video-brand .tag { font-size: 13px; letter-spacing: 1px; color: var(--navy); margin-top: 4px; }
  .video-play { position: absolute; left: 11px; top: 274px; width: 58px; height: 35px; border-radius: 3px; background: var(--video-dark); }
  .video-bar { position: absolute; left: 77px; top: 279px; width: 312px; height: 30px; border-radius: 3px; background: var(--video-dark); }
  .video-track { position: absolute; left: 6px; top: 9px; width: 232px; height: 11px; background: var(--white); border: 1px solid #999; }
  .video-track .loaded { position: absolute; left: 0; top: 2px; height: 6px; width: 190px; background: #666; }
  .video-track .played { position: absolute; left: 0; top: 2px; height: 6px; width: 88px; background: var(--blue); }
  .video-hd { position: absolute; left: 268px; top: 7px; color: var(--blue); font-size: 12px; font-weight: 700; }

  /* Features */
  .features { position: absolute; left: 0; top: 515px; width: 1200px; height: 257px; background: var(--page); border-bottom: 1px solid #e2e2e2; }
  .features h2 { position: absolute; left: 142px; top: 15px; font-size: 25px; font-weight: 700; color: #333; }
  .features .lead { position: absolute; left: 141px; top: 53px; width: 300px; font-size: 16px; line-height: 23px; color: #333; }
  .features .body { position: absolute; left: 142px; top: 105px; width: 290px; font-size: 12.5px; line-height: 18.3px; color: var(--muted); }
  .btn-more { position: absolute; left: 141px; top: 204px; width: 93px; height: 24px; background: var(--gold); color: var(--white);
    font-family: "Lato", sans-serif; font-weight: 700; font-size: 12px; line-height: 24px; text-align: center; }
  .feature { position: absolute; width: 200px; }
  .feature svg { position: absolute; left: 0; top: 0; }
  .feature h3 { margin-left: 43px; font-size: 16px; font-weight: 400; color: #222; line-height: 20px; }
  .feature h3 span { color: var(--gold-dark); }
  .feature p { margin-left: 43px; margin-top: 3px; font-size: 12.5px; line-height: 16px; color: var(--muted); }

  /* Call to action */
  .cta { position: absolute; left: 0; top: 772px; width: 1200px; height: 116px; text-align: center; }
  .cta p { margin-top: 15px; font-size: 25px; color: #333; }
  .btn-signup { position: absolute; left: 506px; top: 60px; width: 189px; height: 38px; border-radius: 19px;
    background: linear-gradient(#fbf08a, #e5cd3a); border: 1px solid #d8c040; box-shadow: 0 2px 3px rgba(0,0,0,.15);
    font-family: "Lato", sans-serif; font-weight: 900; font-size: 19px; line-height: 36px; color: #222; }

  /* Footer */
  .site-footer { position: absolute; left: 0; top: 888px; width: 1200px; height: 154px; background: var(--footer); color: var(--white); }
  .footer-brand { position: absolute; left: 150px; top: 52px; width: 148px; text-align: center; }
  .footer-brand .square { width: 40px; height: 40px; background: var(--white); margin: -44px auto 8px; }
  .footer-brand .name { font-size: 26px; font-weight: 600; letter-spacing: 2px; line-height: 1; }
  .footer-brand .tag { font-size: 8px; letter-spacing: .5px; margin-top: 3px; }
  .footer-col { position: absolute; top: 17px; }
  .footer-col h4 { font-size: 22px; font-weight: 400; padding-bottom: 6px; border-bottom: 1px solid #666; }
  .footer-col ul { list-style: none; margin-top: 8px; }
  .footer-col li { font-size: 13px; line-height: 21px; padding-left: 13px; position: relative; }
  .footer-col li::before { content: "›"; position: absolute; left: 0; top: -1px; }
  .social li { padding-left: 30px; line-height: 31px; font-size: 13.5px; }
  .social li::before { content: ""; width: 20px; height: 20px; top: 6px; background: var(--blue); }
  .copyright { position: absolute; left: 0; top: 1042px; width: 1200px; height: 38px; background: var(--gold);
    color: #fff8e8; font-size: 14px; text-align: center; line-height: 38px; }
</style>
</head>
<body>
  <header class="site-header">
    <div class="brand">
      <div class="brand-square"></div>
      <div>
        <div class="brand-name">VALTORIA</div>
        <div class="brand-tag">SMARTER FINANCIAL STRATEGIES</div>
      </div>
    </div>
    <div class="login">LOGIN</div>
    <nav class="main-nav">
      <a class="active" href="#" style="left:620px">FEATURES</a>
      <a href="#" style="left:759px">EXAMPLES</a>
      <a href="#" style="left:896px">FAQ</a>
      <a href="#" style="left:991px">ABOUT</a>
    </nav>
  </header>

  <section class="hero">
    <div class="hero-photo" role="img" aria-label="Blurred photo of a financial planner at a desk with papers"></div>

    <div class="intro-panel">
      <div class="intro-band"></div>
      <div class="intro-title">Smarter Financial Stratigies</div>
      <p class="intro-lead">Values and Cash-flow focused financial software for financial planners</p>
      <div class="btn-tour">FEATURE TOUR</div>
      <div class="audience-card" style="left:20px">
        <div class="label">FOR PLANNING PRACTICES</div>
        <div class="photo" role="img" aria-label="Photo of a smiling team of financial planners in an office"></div>
      </div>
      <div class="audience-card" style="left:245px">
        <div class="label">FOR DEALER GROUPS</div>
        <div class="photo" role="img" aria-label="Photo of business people in a meeting"></div>
      </div>
    </div>

    <div class="video-panel">
      <div class="video-thumb"></div>
      <div class="video-title">Smarter Financial Strategies</div>
      <div class="video-from">from <span>Valtoria</span></div>

      <div class="video-action" style="top:29px"><svg width="14" height="12" viewBox="0 0 14 12"><path d="M7 12 1 6A3.2 3.2 0 0 1 7 2a3.2 3.2 0 0 1 6 4z" fill="#fff"/></svg>LIKE</div>
      <div class="video-action" style="top:64px"><svg width="14" height="14" viewBox="0 0 14 14"><circle cx="7" cy="7" r="7" fill="#fff"/></svg>LATER</div>
      <div class="video-action" style="top:100px"><svg width="14" height="12" viewBox="0 0 14 12"><circle cx="3" cy="6" r="2" fill="#fff"/><circle cx="11" cy="2" r="2" fill="#fff"/><circle cx="11" cy="10" r="2" fill="#fff"/><path d="M3 6 11 2M3 6l8 4" stroke="#fff"/></svg>SHARE</div>
      <div class="video-action" style="top:135px"><svg width="16" height="12" viewBox="0 0 16 12"><path d="M5 2 1 6l4 4M11 2l4 4-4 4M9 1 7 11" stroke="#fff" stroke-width="1.6" fill="none"/></svg>EMBED</div>

      <div class="video-brand">
        <div class="name">VALTORIA</div>
        <div class="tag">SMARTER FINANCIAL STRATEGIES</div>
      </div>

      <div class="video-play"><svg width="58" height="35" viewBox="0 0 58 35"><path d="M23 10v15l13-7.5z" fill="#fff"/></svg></div>
      <div class="video-bar">
        <div class="video-track"><div class="loaded"></div><div class="played"></div></div>
        <svg class="abs" style="left:244px;top:9px" width="22" height="12" viewBox="0 0 22 12"><g fill="#1a9ad6"><rect x="0" width="2" height="12"/><rect x="4" width="2" height="12"/><rect x="8" width="2" height="12"/><rect x="12" width="2" height="12"/><rect x="16" width="2" height="12"/><rect x="20" width="2" height="12"/></g></svg>
        <div class="video-hd">HD</div>
        <svg class="abs" style="left:293px;top:9px" width="12" height="12" viewBox="0 0 12 12"><path d="M1 1l10 10M11 1 1 11M1 1h4M1 1v4M11 11H7M11 11V7" stroke="#fff" stroke-width="1.6"/></svg>
      </div>
    </div>
  </section>

  <section class="features">
    <h2>Latest Features</h2>
    <p class="lead">Lorem ipsum dolor sit am consectetuer adipisci elit, sed diam nonummy.</p>
    <p class="body">Ut laoreet dolore magna aliquam erat volutpa Ut wisi enim ad minim veni quis nostrud exer tation ullamcorper suscipit lobortis nisl ut ali commodo consequat. Duis autem vel eum iriure d hendrerit in vulputate velit esse molestie consequat.</p>
    <div class="btn-more">READ MORE ››</div>

    <div class="feature" style="left:458px;top:56px">
      <svg width="34" height="36" viewBox="0 0 34 36"><path d="M1 1h32v20L17 35 1 21z" fill="#8a5a12"/><path d="M9 15a8 6 0 0 1 16 0zM17 15v7a2 2 0 0 1-3 0" stroke="#fff" stroke-width="1.5" fill="none"/></svg>
      <h3>Personal <span>Insurance</span></h3>
      <p>Lorem ipsum dolo amet, adipiscing elit, nonummy nibh tincidunt.</p>
    </div>
    <div class="feature" style="left:665px;top:56px">
      <svg width="34" height="36" viewBox="0 0 34 36"><path d="M1 1h32v20L17 35 1 21z" fill="#8a5a12"/><circle cx="17" cy="12" r="4" fill="#fff"/><path d="M10 24a7 6 0 0 1 14 0z" fill="#fff"/></svg>
      <h3>Business <span>Risk</span></h3>
      <p>Lorem ipsum dolo amet, adipiscing elit, nonummy nibh tincidunt.</p>
    </div>
    <div class="feature" style="left:871px;top:56px">
      <svg width="34" height="36" viewBox="0 0 34 36"><path d="M1 1h32v20L17 35 1 21z" fill="#8a5a12"/><circle cx="17" cy="16" r="5" stroke="#fff" stroke-width="1.5" fill="none"/><g fill="#fff"><circle cx="17" cy="7" r="1.5"/><circle cx="8" cy="16" r="1.5"/><circle cx="26" cy="16" r="1.5"/><circle cx="11" cy="10" r="1.5"/><circle cx="23" cy="10" r="1.5"/></g></svg>
      <h3>Self <span>Managed</span></h3>
      <p>Lorem ipsum dolo amet, adipiscing elit, nonummy nibh tincidunt.</p>
    </div>
    <div class="feature" style="left:458px;top:157px">
      <svg width="34" height="36" viewBox="0 0 34 36"><path d="M1 1h32v20L17 35 1 21z" fill="#8a5a12"/><circle cx="17" cy="15" r="7" stroke="#fff" stroke-width="1.5" fill="none"/><text x="17" y="19" text-anchor="middle" font-size="10" fill="#fff" font-family="Open Sans, sans-serif">$</text></svg>
      <h3>Credit <span>Services</span></h3>
      <p>Lorem ipsum dolo amet, adipiscing elit, nonummy nibh tincidunt.</p>
    </div>
    <div class="feature" style="left:665px;top:157px">
      <svg width="34" height="36" viewBox="0 0 34 36"><path d="M1 1h32v20L17 35 1 21z" fill="#8a5a12"/><path d="M13 7h8l-2 4a7 7 0 1 1-4 0z" fill="#fff"/><text x="17" y="21" text-anchor="middle" font-size="9" fill="#8a5a12" font-family="Open Sans, sans-serif">$</text></svg>
      <h3>Budget <span>Planner</span></h3>
      <p>Lorem ipsum dolo amet, adipiscing elit, nonummy nibh tincidunt.</p>
    </div>
    <div class="feature" style="left:871px;top:157px">
      <svg width="34" height="36" viewBox="0 0 34 36"><path d="M1 1h32v20L17 35 1 21z" fill="#8a5a12"/><circle cx="17" cy="16" r="5" stroke="#fff" stroke-width="1.5" fill="none"/><g fill="#fff"><circle cx="17" cy="7" r="1.5"/><circle cx="8" cy="16" r="1.5"/><circle cx="26" cy="16" r="1.5"/><circle cx="11" cy="10" r="1.5"/><circle cx="23" cy="10" r="1.5"/></g></svg>
      <h3>Snap <span>Shot</span></h3>
      <p>Lorem ipsum dolo amet, adipiscing elit, nonummy nibh tincidunt.</p>
    </div>
  </section>

  <section class="cta">
    <p>Create an account today and begin your <strong>30 day Trial!</strong></p>
    <div class="btn-signup">SIGN UP NOW !</div>
  </section>

  <footer class="site-footer">
    <div class="footer-brand">
      <div class="square"></div>
      <div class="name">VALTORIA</div>
      <div class="tag">SMARTER FINANCIAL STRATEGIES</div>
    </div>
    <div class="footer-col" style="left:352px;width:100px">
      <h4>About</h4>
      <ul><li>About Us</li><li>Support</li></ul>
    </div>
    <div class="footer-col" style="left:516px;width:161px">
      <h4>Getting Started</h4>
      <ul><li>Why Valtoria</li><li>Download &amp; Summary</li><li>Valtoria Videos</li></ul>
    </div>
    <div class="footer-col" style="left:738px;width:100px">
      <h4>Legal</h4>
      <ul><li>Tearms of Use</li><li>Privacy</li></ul>
    </div>
    <div class="footer-col social" style="left:896px;width:163px">
      <h4>Socail Connect</h4>
      <ul><li>Valtoria on Linkora</li><li>Valtoria on Chirpwave</li></ul>
    </div>
  </footer>
  <div class="copyright">Copyright © 2014 Valtoria Pty Ltd. All right Reserved</div>
</body>
</html>
```